Either a trifold or double sided flyer/brochure

A flyer to help spark interest in a historic preservation project in Ashbrook, NH--looking for something that captures the early 19th century rural village and mill times--American Primitive, Shaker, Cross Stitch Sampler...must be able to highlight home history as well as have all owners of house on a single page. Word document attached--can also provide files for the house painting, color photos, dorne photo, advertising photo or part of original settler map.
I like this brochure
http://tessavolkind.com/wordpress/quarnby-lodge-museum-brochure/
community stakeholders, residents,
Historic Preservation, House Museums.

```html
<!DOCTYPE html>
<html lang="en">
<head>
<meta charset="utf-8">
<title>The Hollister Homestead History c. 1826</title>
<link href="https://fonts.googleapis.com/css2?family=Oswald:wght@500;600&family=Roboto:wght@400;500&display=swap" rel="stylesheet">
<style>
  :root {
    --backdrop: #3a3a3c;
    --navy: #13263f;
    --gold: #c8902e;
    --parchment: #ede8e2;
    --parchment-deep: #e2dbd2;
    --ink: #2b2b2b;
    --caption-blue: #2350a0;
    --rule: #c9bfb2;
    --white: #ffffff;
  }
  * { box-sizing: border-box; margin: 0; padding: 0; }
  html, body { width: 1200px; height: 900px; overflow: hidden; }
  body { background: var(--backdrop); font-family: "Roboto", Arial, sans-serif; color: var(--ink); position: relative; }

  .page {
    position: absolute; top: 100px; width: 540px; height: 700px;
    background: linear-gradient(180deg, var(--parchment), var(--parchment-deep));
    overflow: hidden; box-shadow: 0 10px 30px rgba(0,0,0,.45);
  }
  .page--history { left: 30px; }
  .page--owners { left: 630px; }

  .hero { position: absolute; left: 0; top: 0; width: 540px; height: 285px; }
  .hero--autumn { background: linear-gradient(160deg, #2f3a1c 0%, #6b6a2a 30%, #c9a445 52%, #b46a2a 70%, #3f4a24 100%); }
  .hero--winter { background: linear-gradient(170deg, #b9bec2 0%, #8e8f86 35%, #c8a83e 55%, #e9ebee 75%, #f4f5f6 100%); }
  .hero-shade { position: absolute; left: 0; top: 0; width: 300px; height: 285px; background: linear-gradient(90deg, rgba(0,0,0,.55), rgba(0,0,0,0)); }

  .paper-edge { position: absolute; left: 0; width: 540px; display: block; }

  .title { position: absolute; left: 30px; top: 90px; color: var(--white); font-family: "Oswald", Arial, sans-serif; font-weight: 600; text-transform: uppercase; }
  .title h1 { font-size: 30px; line-height: 32px; letter-spacing: .5px; }
  .title p { font-size: 13px; font-weight: 500; margin-top: 8px; letter-spacing: .3px; }

  .snapshot { position: absolute; background: var(--white); padding: 5px; box-shadow: 0 3px 8px rgba(0,0,0,.35); }
  .snapshot span { display: block; width: 100%; height: 100%; }
  .snapshot--family { left: 340px; top: 190px; width: 122px; height: 96px; }
  .snapshot--family span { background: linear-gradient(135deg, #8d8377, #4a443e); }
  .snapshot--portrait { left: 465px; top: 180px; width: 112px; height: 100px; }
  .snapshot--portrait span { background: linear-gradient(135deg, #a59a86, #5f564a); }

  .history { position: absolute; left: 26px; top: 300px; width: 488px; }
  .section-title { font-family: "Oswald", Arial, sans-serif; font-weight: 500; color: var(--gold); text-transform: uppercase; font-size: 12px; letter-spacing: .3px; margin-bottom: 8px; }
  .history p { font-size: 6.9px; line-height: 9.2px; margin-bottom: 6px; text-align: justify; }

  .footer { position: absolute; left: 0; bottom: 0; width: 540px; height: 68px; background: var(--navy); }
  .footer-invite { position: absolute; left: 30px; bottom: 18px; display: flex; align-items: center; gap: 10px; color: var(--gold); font-size: 9px; }
  .footer-invite i { width: 22px; height: 22px; border-radius: 50%; background: var(--gold); display: block; }

  .painting { position: absolute; left: 380px; top: 170px; width: 150px; height: 118px; background: var(--white); padding: 7px; box-shadow: 0 4px 10px rgba(0,0,0,.35); }
  .painting span { display: block; width: 100%; height: 100%; background: linear-gradient(180deg, #2b4a6e 0%, #3c5a86 40%, #e8ecf2 55%, #3b54a3 70%, #56693e 100%); }

  .owners { position: absolute; left: 26px; top: 312px; width: 330px; }
  .owners .section-title { line-height: 14px; margin-bottom: 6px; }
  .owner-row { display: flex; justify-content: space-between; align-items: flex-end; border-bottom: 1px dotted var(--rule); height: 30px; padding-bottom: 5px; font-size: 8px; line-height: 10px; }
  .owner-row .year { color: var(--gold); font-size: 9px; white-space: nowrap; margin-left: 10px; }
  .owner-row small { font-size: 7.4px; }

  .side { position: absolute; left: 370px; top: 300px; width: 155px; }
  .thumb { position: absolute; background: var(--white); padding: 4px; box-shadow: 0 3px 8px rgba(0,0,0,.3); }
  .thumb span { display: block; width: 100%; height: 100%; }
  .thumb--stairs { left: 0; top: 0; width: 76px; height: 70px; }
  .thumb--stairs span { background: linear-gradient(135deg, #efe9df, #8a4f2a); }
  .thumb--gable { left: 64px; top: 14px; width: 86px; height: 80px; }
  .thumb--gable span { background: linear-gradient(160deg, #3d6fb0, #d9b43a 55%, #6e5a2a); }
  .side-caption { position: absolute; left: 0; top: 112px; width: 155px; text-align: center; color: var(--caption-blue); font-size: 8.5px; line-height: 12px; }
  .settler-map { position: absolute; left: 8px; top: 160px; width: 140px; height: 120px; background: linear-gradient(135deg, #e6e4df, #bdbab3); border: 1px solid #9d9a93; }
  .mill-ad { position: absolute; left: 20px; top: 290px; width: 120px; height: 40px; background: linear-gradient(180deg, #f4f2ee, #d8d4cc); }
</style>
</head>
<body>

<article class="page page--history">
  <div class="hero hero--autumn" role="img" aria-label="Photograph of the yellow clapboard homestead among autumn trees"></div>
  <div class="hero-shade"></div>
  <header class="title">
    <h1>The Hollister<br>Homestead<br>History c. 1826</h1>
    <p>Ashbrook, New Hampshire</p>
  </header>
  <svg class="paper-edge" style="top:255px" width="540" height="40" viewBox="0 0 540 40" aria-hidden="true">
    <polygon fill="#ede8e2" points="0,38 0,24 60,20 120,17 200,13 280,9 360,6 440,3 540,0 540,40 0,40"/>
  </svg>
  <div class="snapshot snapshot--family" role="img" aria-label="Sepia photograph of family members"><span></span></div>
  <div class="snapshot snapshot--portrait" role="img" aria-label="Sepia portrait photograph"><span></span></div>

  <section class="history">
    <h2 class="section-title">The Hollister Homestead History c. 1826</h2>
    <p>In 1826, George S. Hollister and his wife, Jane (Hart) Hollister purchased 26 acres from Robert Pell on the Quill River, north of Varney's Woolen Mill in South Ashbrook, NH. This parcel was carved out lot #32 which was comprised of 268 acres that were deeded to John Pell (Robert Pell's grandfather) by Jeremiah Stowe and John Ames on May 5, 1762.</p>
    <p>It is believed that Hollister, who was blacksmith, built the house that currently stands at 42 Linden Street in Ashbrook, NH. He also built his forge on the site down by the river. It is likely that much of the forged hardware in the home was crafted by him. Feeling the need to leave Ashbrook for a new frontier, Hollister left town with his brother, Barlow, to purchase land in the emerging communities of Orleans County, NY. Before doing so, Hollister sold the home, shop and buildings to Thomas Garner and his wife Alice (Reed) Garner in 1828.</p>
    <p>By trade, Thomas Garner was a cloth dresser and wool-carder. He was also a deeply religious man and served as deacon in the emerging, but still quite small, Baptist community. In those days, small groups of the Baptists and Methodists met in the Chandler Home for bible study, prayers and singing. The Chandlers were well known abolitionists and their house served as a stop on the Underground Railroad. Deacon Garner died in 1839 and his estate was managed by Samuel Reed—very likely a relative of Alice—who protected Alice's dower. The property was then sold to Elijah Brown Ashford and his wife Achsah (Lowe) Ashford. Elijah was quite industrious and continued to expand the wool mill. He was an early investor in the Granite Ridge Railroad and ceded a right of way to the railroad on the homestead. The mill eventually came under the control of his son, Henry A. Ashford, and operated until it burned down on April 20, 1874. Elijah passed away in 1877 and left the home to Mary Ellen Ashford who was most commonly known as "Ellen."</p>
    <p>Ellen Ashford was approached in 1891 by Allie Varney, the owner of the Varney's Mill Complex, to ask if she would be willing to rent out the home to a couple from Boston. This turned out to be Marian and Edward Fairlie, the founders of the Fairlie Colony, who ended up spending their first summer in Ashbrook, NH in the home. Marian recalls in her writings: "You can't fail to remember the two-story farmhouse almost across the road from the iron bridge, now occupied by the Dorne Family. It had never been painted and was a lovely soft gray in color. There were really only four rooms and a kitchen, spotlessly clean and adequately furnished, which really didn't mean much but some chairs, tables and beds. Then in the kitchen was something that fascinated me, a stone bowl into which the clearest of water was all the time pouring and then running off into a drain…"</p>
    <p>The Dornes lived in this home for the longest time of any owner—and some refer to this area before the bridge, as Dornes Corner. This moment of stewardship began under Fred Parker Dorne and his wife Grace E. (Holt) Dorne around 1904 and lasted until 2015 when a descendant sold the home. The house is now under the stewardship of Edward M. Calloway and Albert A. Pritchard, Jr. and will be undergoing a significant restoration.</p>
  </section>

  <footer class="footer">
    <svg class="paper-edge" style="top:-1px" width="540" height="16" viewBox="0 0 540 16" aria-hidden="true">
      <polygon fill="#e2dbd2" points="0,0 540,0 540,8 520,12 505,6 488,13 470,7 450,14 430,8 410,12 392,5 372,13 352,8 332,14 312,6 292,12 272,7 252,14 232,8 212,12 192,5 172,13 152,8 132,14 112,6 92,12 72,7 52,14 32,8 14,12 0,6"/>
    </svg>
    <div class="footer-invite"><i></i>They invite you to join their Hearthside Group</div>
  </footer>
</article>

<article class="page page--owners">
  <div class="hero hero--winter" role="img" aria-label="Photograph of the yellow homestead and barn in falling snow"></div>
  <svg class="paper-edge" style="top:262px" width="540" height="30" viewBox="0 0 540 30" aria-hidden="true">
    <polygon fill="#ede8e2" points="0,10 90,12 180,14 270,16 360,18 540,20 540,30 0,30"/>
  </svg>
  <div class="painting" role="img" aria-label="Painting of the homestead in blue and white"><span></span></div>

  <section class="owners">
    <h2 class="section-title">Of 42 Linden Street<br>Ashbrook, New Hampshire</h2>
    <div class="owner-row"><span>Robert Pell (grandson of John Pell) owned the land</span><span class="year">1826</span></div>
    <div class="owner-row"><span>George S. Hollister and Jane (Hart) Hollister</span><span class="year">1826-1828</span></div>
    <div class="owner-row"><span>Deacon Thomas Garner and Alice (Reed) Garner (Baptist)</span><span class="year">1828-1839</span></div>
    <div class="owner-row"><span>Elijah Brown Ashford and Achsah (Lowe) Ashford<br><small>(mortgage between Samuel Reed and Ashford is 1845)</small></span><span class="year">1839-1877</span></div>
    <div class="owner-row"><span>Mary Ellen Ashford</span><span class="year">1877-1898</span></div>
    <div class="owner-row"><span>James Merrow</span><span class="year">1898-1904</span></div>
    <div class="owner-row"><span>Fred Parker Dorne and Grace E. (Holt) Dorne</span><span class="year">1904-1956</span></div>
    <div class="owner-row"><span>Elinor (Dorne) Thornley and Frank O Thornley<br><small>(Elinor was born in house on July 29, 1911)</small></span><span class="year">1955-1998</span></div>
    <div class="owner-row"><span>James H. Vanderlin and Maria Ortiz Vanderlin<br><small>(James was nephew of Elinor (Dorne) Thornley)</small></span><span class="year">1998-2015</span></div>
    <div class="owner-row"><span>Millbrook Commons</span><span class="year">2015-2022</span></div>
    <div class="owner-row"><span>Edward M. Calloway and Albert A. Pritchard, Jr.</span><span class="year">2022</span></div>
  </section>

  <aside class="side">
    <div class="thumb thumb--stairs" role="img" aria-label="Photograph of the interior staircase"><span></span></div>
    <div class="thumb thumb--gable" role="img" aria-label="Photograph of the yellow gable end under blue sky"><span></span></div>
    <p class="side-caption">Hollister Homestead c. 1826,<br>Dornes Corner, Ashbrook,<br>New Hampshire</p>
    <div class="settler-map" role="img" aria-label="Section of the early settler map showing the homestead lots"></div>
    <div class="mill-ad" role="img" aria-label="Antique newspaper advertisement for the wool carder and cloth dresser"></div>
  </aside>

  <footer class="footer">
    <svg class="paper-edge" style="top:-1px" width="540" height="16" viewBox="0 0 540 16" aria-hidden="true">
      <polygon fill="#e2dbd2" points="0,0 540,0 540,6 522,13 502,7 484,12 464,5 444,13 424,8 404,14 384,6 364,12 344,7 324,14 304,8 284,12 264,5 244,13 224,8 204,14 184,6 164,12 144,7 124,14 104,8 84,12 64,5 44,13 24,8 0,12"/>
    </svg>
    <div class="footer-invite"><i></i>They invite you to join their Hearthside Group</div>
  </footer>
</article>

</body>
</html>
```